HOLLOWAY PINE SERVICES INC. | ||
HOLLOWAY PINE SERVICES INC.COM | ||
Cutting-Edge Corporate Modern Professional |
Lionel Fabre | ||
HOLLOWAY PINE SERVICESINC. | ||
There is no address! Thank you | ||
HOLLOWAYPINESERVICESINC@ORVELMAIL.COM | ||
HOLLOWAYPINESERVICESINC.COM | ||
I want my logo to be used with all my stationary. Thank You. | ||
Im open to anything that looks good | ||
Logo_4353.jpg i like for my stationary to have a light colored look1 not a dark color tint. light n ritch in color |

```html
<!DOCTYPE html>
<html lang="en">
<head>
<meta charset="utf-8">
<title>Holloway Pine Services Inc. – Business Card</title>
<link href="https://fonts.googleapis.com/css2?family=Arimo:wght@400;700&display=swap" rel="stylesheet">
<style>
  :root{
    --stage:#3b3b3b;
    --card-light:#f1f8e4;
    --card-mid:#d8edbb;
    --card-deep:#bfe09a;
    --brand-green:#3f9a2c;
    --ink:#2f3a2a;
    --tag-red:#7a1d1d;
    --tag-text:#f5e9e4;
  }
  html,body{margin:0;padding:0;width:1200px;height:926px;overflow:hidden;background:var(--stage);}
  body{font-family:"Arimo",Arial,sans-serif;position:relative;}
  .card{
    position:absolute;top:330px;width:460px;height:263px;border-radius:3px;overflow:hidden;
    background:radial-gradient(ellipse at 30% 40%,var(--card-light) 0%,var(--card-mid) 60%,var(--card-deep) 100%);
    box-shadow:0 6px 18px rgba(0,0,0,.45);
  }
  .card--front{left:120px;}
  .card--back{left:620px;}
  .card-frame{position:absolute;inset:7px;border:1px solid rgba(255,255,255,.75);border-radius:2px;pointer-events:none;}
  .card-swoosh{position:absolute;inset:0;width:100%;height:100%;}
  .brand{position:absolute;display:flex;flex-direction:column;align-items:center;}
  .brand-dot{border-radius:50%;background:var(--brand-green);}
  .brand-name{color:var(--brand-green);font-weight:700;text-align:center;line-height:1.1;letter-spacing:.3px;}
  .card--front .brand{left:28px;top:86px;width:150px;}
  .card--front .brand-dot{width:46px;height:46px;margin-bottom:10px;}
  .card--front .brand-name{font-size:15px;}
  .name-tag{position:absolute;left:320px;top:26px;background:var(--tag-red);color:var(--tag-text);font-size:10px;padding:4px 9px;}
  .features{position:absolute;left:200px;top:64px;width:230px;margin:0;padding:0 0 0 12px;color:var(--ink);font-size:10.5px;line-height:1.45;}
  .features li{margin-bottom:2px;}
  .card--back .brand{left:0;right:0;top:40px;}
  .card--back .brand-dot{width:38px;height:38px;margin-bottom:8px;}
  .card--back .brand-name{font-size:13px;}
  .contacts{position:absolute;left:60px;top:168px;margin:0;padding:0;list-style:none;color:var(--ink);font-size:11px;line-height:1.75;}
  .contacts li{display:flex;align-items:center;gap:8px;}
  .contacts svg{width:11px;height:11px;flex:none;}
</style>
</head>
<body>

<section class="card card--front" aria-label="Business card front">
  <svg class="card-swoosh" viewBox="0 0 460 263" preserveAspectRatio="none" aria-hidden="true">
    <path d="M0 200 C140 150 300 260 460 170 L460 263 L0 263 Z" fill="#ffffff" opacity=".22"/>
    <path d="M0 40 C160 90 300 0 460 50 L460 0 L0 0 Z" fill="#ffffff" opacity=".18"/>
  </svg>
  <div class="card-frame"></div>
  <div class="brand">
    <div class="brand-dot"></div>
    <div class="brand-name">HOLLOWAY PINE<br>SERVICES INC.COM</div>
  </div>
  <div class="name-tag">Lionel Fabre</div>
  <ul class="features">
    <li>Operating in Strict Compliance with CA. Prop 215 &amp; SB 420.</li>
    <li>Qualified Patients Only.</li>
    <li>Speedy Delivery Service.</li>
    <li>Clones Available.</li>
    <li>5 Gram Eighths for First Time Patients &amp; Referrals.</li>
    <li>Open Monday-Sunday 8am-8pm.</li>
  </ul>
</section>

<section class="card card--back" aria-label="Business card back">
  <svg class="card-swoosh" viewBox="0 0 460 263" preserveAspectRatio="none" aria-hidden="true">
    <path d="M0 200 C140 150 300 260 460 170 L460 263 L0 263 Z" fill="#ffffff" opacity=".22"/>
    <path d="M0 40 C160 90 300 0 460 50 L460 0 L0 0 Z" fill="#ffffff" opacity=".18"/>
  </svg>
  <div class="card-frame"></div>
  <div class="brand">
    <div class="brand-dot"></div>
    <div class="brand-name">HOLLOWAY PINE<br>SERVICES INC.COM</div>
  </div>
  <ul class="contacts">
    <li><svg viewBox="0 0 12 12" aria-hidden="true"><path d="M3 1 L5 3.5 L4 5 C5 7 6 8 7 8.5 L8.5 7.5 L11 9.5 L9.5 11 C5 11 1 7 1 2.5 Z" fill="var(--ink)"/></svg>(555) 734-9182</li>
    <li><svg viewBox="0 0 12 12" aria-hidden="true"><rect x="2" y="1" width="8" height="4" fill="none" stroke="var(--ink)"/><rect x="1" y="5" width="10" height="5" fill="var(--ink)"/></svg>(555) 416-2750</li>
    <li><svg viewBox="0 0 12 12" aria-hidden="true"><rect x="1" y="2.5" width="10" height="7" fill="none" stroke="var(--ink)"/><path d="M1 2.5 L6 6.5 L11 2.5" fill="none" stroke="var(--ink)"/></svg>hollowaypineservicesinc@orvelmail.com</li>
    <li><svg viewBox="0 0 12 12" aria-hidden="true"><circle cx="6" cy="6" r="4.8" fill="none" stroke="var(--ink)"/><path d="M1.2 6 H10.8 M6 1.2 C3.5 4 3.5 8 6 10.8 M6 1.2 C8.5 4 8.5 8 6 10.8" fill="none" stroke="var(--ink)" stroke-width=".8"/></svg>hollowaypineservicesinc.com</li>
  </ul>
</section>

</body>
</html>
```